Brantwell Group needs a business card design

We need a new business card design using the logo recently selected in a logo competition on Pixel Forum. Our business is a consultancy specializing in aviation and energy and the winning business card design will promote an image of precision and professionalism with creativity.

Please use the logo with the name on the front of the card and use a complementary font. Make the back white with either the light grey or dark grey logo.

Target Market(s)

Senior finance and legal leaders at aviation and energy companies

Industry/Entity Type

Management Consulting

Contact Information for Business Card

Peter Haldane
President
Brantwell Group

www.brantwellgroup.example

(555) 304-6198
ph@brantwellgroup.example

Requirements
Must have
• Professional font that goes well with the logo font

```html
<!DOCTYPE html>
<html lang="en">
<head>
<meta charset="utf-8">
<title>Brantwell Group – Business Cards</title>
<link rel="stylesheet" href="https://fonts.googleapis.com/css2?family=Questrial&display=swap">
<style>
  :root {
    --page-bg: #2a2a2a;
    --card-light: #c9c9c9;
    --card-dark: #141414;
    --text-on-light: #5e5e5e;
    --text-on-dark: #d8d8d8;
    --mark-light: #1c1c1c;
    --mark-dark: #2c2c2c;
  }
  * { box-sizing: border-box; margin: 0; padding: 0; }
  html, body {
    width: 1200px; height: 848px; overflow: hidden;
    background: var(--page-bg);
    font-family: "Questrial", "Century Gothic", sans-serif;
  }
  .canvas { position: relative; width: 1200px; height: 848px; }

  .card {
    position: absolute;
    width: 610px; height: 350px;
    border-radius: 18px;
    display: flex; align-items: center;
    padding: 0 40px 0 50px;
    box-shadow: 0 10px 30px rgba(0,0,0,.45);
  }
  .card--light { left: 290px; top: 50px; background: var(--card-light); color: var(--text-on-light); }
  .card--dark  { left: 460px; top: 445px; background: var(--card-dark); color: var(--text-on-dark); }

  .brand {
    width: 230px; flex: none;
    display: flex; flex-direction: column; align-items: center; gap: 14px;
  }
  .brand__mark { width: 56px; height: 56px; }
  .card--light .brand__mark { background: var(--mark-light); }
  .card--dark .brand__mark { background: var(--mark-dark); }
  .brand__name { font-size: 22px; text-align: center; line-height: 1.2; }

  .contact { margin-left: 20px; white-space: nowrap; }
  .contact__name { font-size: 26px; }
  .contact__title { font-size: 17px; margin: 2px 0 16px 2px; }
  .contact__line { display: flex; align-items: center; gap: 8px; font-size: 16px; margin-bottom: 5px; }
  .contact__icon { width: 20px; height: 14px; fill: currentColor; flex: none; }
</style>
</head>
<body>
<main class="canvas">

  <section class="card card--light" aria-label="Business card, light version">
    <div class="brand">
      <div class="brand__mark"></div>
      <div class="brand__name">Brantwell Group</div>
    </div>
    <div class="contact">
      <p class="contact__name">Peter Haldane</p>
      <p class="contact__title">President</p>
      <p class="contact__line">
        <svg class="contact__icon" viewBox="0 0 20 14" aria-hidden="true"><path d="M1 4c0-2 4-3 9-3s9 1 9 3v2h-4V4H5v2H1zM4 7h12l2 6H2z"/></svg>
        (555) 304-6198
      </p>
      <p class="contact__line">
        <svg class="contact__icon" viewBox="0 0 20 14" aria-hidden="true"><path d="M1 1h18v12H1zM2 2l8 6 8-6" fill="none" stroke="currentColor" stroke-width="1.4"/></svg>
        ph@brantwellgroup.example
      </p>
      <p class="contact__line">
        <svg class="contact__icon" viewBox="0 0 20 14" aria-hidden="true"><circle cx="10" cy="7" r="6" fill="none" stroke="currentColor" stroke-width="1.3"/><path d="M4 7h12M10 1c-3 3-3 9 0 12M10 1c3 3 3 9 0 12" fill="none" stroke="currentColor" stroke-width="1.1"/></svg>
        www.brantwellgroup.example
      </p>
    </div>
  </section>

  <section class="card card--dark" aria-label="Business card, dark version">
    <div class="brand">
      <div class="brand__mark"></div>
      <div class="brand__name">Brantwell Group</div>
    </div>
    <div class="contact">
      <p class="contact__name">Peter Haldane</p>
      <p class="contact__title">President</p>
      <p class="contact__line">
        <svg class="contact__icon" viewBox="0 0 20 14" aria-hidden="true"><path d="M1 4c0-2 4-3 9-3s9 1 9 3v2h-4V4H5v2H1zM4 7h12l2 6H2z"/></svg>
        (555) 304-6198
      </p>
      <p class="contact__line">
        <svg class="contact__icon" viewBox="0 0 20 14" aria-hidden="true"><path d="M1 1h18v12H1zM2 2l8 6 8-6" fill="none" stroke="currentColor" stroke-width="1.4"/></svg>
        ph@brantwellgroup.example
      </p>
      <p class="contact__line">
        <svg class="contact__icon" viewBox="0 0 20 14" aria-hidden="true"><circle cx="10" cy="7" r="6" fill="none" stroke="currentColor" stroke-width="1.3"/><path d="M4 7h12M10 1c-3 3-3 9 0 12M10 1c3 3 3 9 0 12" fill="none" stroke="currentColor" stroke-width="1.1"/></svg>
        www.brantwellgroup.example
      </p>
    </div>
  </section>

</main>
</body>
</html>
```